Answer Choice Icons

We need four versions of an answer choice icon. We need an A, B, C and D. They need to be 40 by 40 pixels and in .png format. They will be used as the labels for the answer choices on a multiple choice test. The student will click on the A, the B, the C, or D icon to select their answer. I have uploaded an example.

Industry/Entity Type

Student

Requirements
Must have
• 40 x 40 pixels; png format
Nice to have
• An oval shape with some shine would be nice. Also having each one a different color would be good.

```html
<!DOCTYPE html>
<html lang="en">
<head>
<meta charset="utf-8">
<title>Find the Area of the Rectangle</title>
<link rel="stylesheet" href="https://fonts.googleapis.com/css2?family=Fredoka:wght@700&family=Libre+Baskerville:wght@400;700&display=swap">
<style>
  :root {
    --page: #ffffff;
    --frame: #8c8c8c;
    --title: #c8141e;
    --ink: #333333;
    --choice-a: #1b9be2;
    --choice-b: #6b61aa;
    --choice-c: #d8cc1c;
    --choice-d: #d8288e;
    --tile-edge: #7d7a22;
    --tile-light: #f4f1b6;
    --tile-mid: #d8d043;
    --tile-dark: #b7ad1e;
  }
  * { box-sizing: border-box; margin: 0; padding: 0; }
  html, body { width: 1200px; height: 705px; overflow: hidden; background: var(--page); }
  .canvas { position: relative; width: 1200px; height: 705px; }
  .card {
    position: absolute; left: 22px; top: 15px; width: 1152px; height: 668px;
    border: 3px solid var(--frame); border-radius: 22px; background: var(--page);
  }
  .question {
    position: absolute; left: 0; right: 0; top: 18px; text-align: center;
    font-family: "Libre Baskerville", Georgia, serif; font-size: 27px; color: var(--title);
  }
  .choice { position: absolute; left: 22px; height: 70px; display: flex; align-items: center; }
  .choice-letter {
    width: 66px; text-align: center;
    font-family: "Fredoka", "Arial Rounded MT Bold", sans-serif; font-weight: 700; font-size: 40px;
  }
  .choice-a { top: 90px; } .choice-a .choice-letter { color: var(--choice-a); }
  .choice-b { top: 245px; } .choice-b .choice-letter { color: var(--choice-b); }
  .choice-c { top: 381px; } .choice-c .choice-letter { color: var(--choice-c); }
  .choice-d { top: 522px; } .choice-d .choice-letter { color: var(--choice-d); }
  .choice-orb { width: 70px; height: 80px; margin-left: 5px; margin-top: 12px; }
  .choice-text {
    margin-left: 68px; font-family: "Libre Baskerville", Georgia, serif;
    font-size: 25px; color: var(--ink);
  }
  .tile {
    width: 53px; height: 53px; border-radius: 11px; border: 2px solid var(--tile-edge);
    background: linear-gradient(135deg, var(--tile-dark) 0%, var(--tile-mid) 40%, var(--tile-light) 100%);
    box-shadow: inset 2px 2px 0 rgba(255,255,255,0.35);
  }
  .legend { position: absolute; left: 550px; top: 302px; display: flex; align-items: center; gap: 12px; }
  .legend-text { font-family: "Libre Baskerville", Georgia, serif; font-size: 25px; color: var(--ink); }
  .rectangle {
    position: absolute; left: 879px; top: 42px;
    display: grid; grid-template-columns: repeat(3, 53px); grid-auto-rows: 53px; gap: 4px;
  }
</style>
</head>
<body>
<div class="canvas">
  <svg width="0" height="0" style="position:absolute">
    <defs>
      <radialGradient id="orb-blue" cx="50%" cy="60%" r="55%"><stop offset="0" stop-color="#7fd6ff"/><stop offset="0.6" stop-color="#1f95d8"/><stop offset="1" stop-color="#0b4f86"/></radialGradient>
      <radialGradient id="orb-purple" cx="50%" cy="60%" r="55%"><stop offset="0" stop-color="#a59be0"/><stop offset="0.6" stop-color="#4d4496"/><stop offset="1" stop-color="#231c5a"/></radialGradient>
      <radialGradient id="orb-yellow" cx="50%" cy="60%" r="55%"><stop offset="0" stop-color="#f4f0a6"/><stop offset="0.6" stop-color="#b9b23a"/><stop offset="1" stop-color="#6d6818"/></radialGradient>
      <radialGradient id="orb-pink" cx="50%" cy="60%" r="55%"><stop offset="0" stop-color="#ff9fd3"/><stop offset="0.6" stop-color="#d2268a"/><stop offset="1" stop-color="#7e0c4f"/></radialGradient>
      <linearGradient id="orb-shine" x1="0" y1="0" x2="0" y2="1"><stop offset="0" stop-color="#fff" stop-opacity="0.85"/><stop offset="1" stop-color="#fff" stop-opacity="0.05"/></linearGradient>
      <radialGradient id="orb-shadow"><stop offset="0" stop-color="#9a9a9a" stop-opacity="0.7"/><stop offset="1" stop-color="#9a9a9a" stop-opacity="0"/></radialGradient>
      <symbol id="orb-rim" viewBox="0 0 70 80">
        <ellipse cx="35" cy="73" rx="27" ry="5" fill="url(#orb-shadow)"/>
        <circle cx="35" cy="34" r="31" fill="#e8e8ee" stroke="#c4c4cc" stroke-width="1.5"/>
      </symbol>
    </defs>
  </svg>

  <div class="card">
    <h1 class="question">Question: Find the are of the rectangle.</h1>

    <div class="choice choice-a">
      <span class="choice-letter">A</span>
      <svg class="choice-orb" viewBox="0 0 70 80"><use href="#orb-rim"/><circle cx="35" cy="34" r="26" fill="url(#orb-blue)"/><ellipse cx="35" cy="22" rx="17" ry="10" fill="url(#orb-shine)"/></svg>
      <span class="choice-text">30 square meters</span>
    </div>
    <div class="choice choice-b">
      <span class="choice-letter">B</span>
      <svg class="choice-orb" viewBox="0 0 70 80"><use href="#orb-rim"/><circle cx="35" cy="34" r="26" fill="url(#orb-purple)"/><ellipse cx="35" cy="22" rx="17" ry="10" fill="url(#orb-shine)"/></svg>
      <span class="choice-text">13 square meters</span>
    </div>
    <div class="choice choice-c">
      <span class="choice-letter">C</span>
      <svg class="choice-orb" viewBox="0 0 70 80"><use href="#orb-rim"/><circle cx="35" cy="34" r="26" fill="url(#orb-yellow)"/><ellipse cx="35" cy="22" rx="17" ry="10" fill="url(#orb-shine)"/></svg>
      <span class="choice-text">26 square meters</span>
    </div>
    <div class="choice choice-d">
      <span class="choice-letter">D</span>
      <svg class="choice-orb" viewBox="0 0 70 80"><use href="#orb-rim"/><circle cx="35" cy="34" r="26" fill="url(#orb-pink)"/><ellipse cx="35" cy="22" rx="17" ry="10" fill="url(#orb-shine)"/></svg>
      <span class="choice-text">40 square meters</span>
    </div>

    <div class="legend">
      <div class="tile"></div>
      <span class="legend-text">= 1 square meter</span>
    </div>

    <div class="rectangle" aria-label="Rectangle of 3 by 10 unit squares">
      <div class="tile"></div><div class="tile"></div><div class="tile"></div>
      <div class="tile"></div><div class="tile"></div><div class="tile"></div>
      <div class="tile"></div><div class="tile"></div><div class="tile"></div>
      <div class="tile"></div><div class="tile"></div><div class="tile"></div>
      <div class="tile"></div><div class="tile"></div><div class="tile"></div>
      <div class="tile"></div><div class="tile"></div><div class="tile"></div>
      <div class="tile"></div><div class="tile"></div><div class="tile"></div>
      <div class="tile"></div><div class="tile"></div><div class="tile"></div>
      <div class="tile"></div><div class="tile"></div><div class="tile"></div>
      <div class="tile"></div><div class="tile"></div><div class="tile"></div>
    </div>
  </div>
</div>
</body>
</html>
```